Wizards of the Fibbing Crafts Book and ebook cover

The goal out of this is to make 1) a cover for a 5"x8" 170 page book, and then 2) an E book square high resolution cover to be used on Narrafy.

I've attached the files that won the first competition on the book cover - for reference.

This book is called "Wizards of the fibbing crafts" - part 1
It is a comedy/satire about MBAs, education, and a bit of the current environment humor.

I want some thing of this style, but improved/better for this professional, informative, satire, and laugh out loud funny book.

I plan on extending the deadline for folks since I've seen a lot of intent to submit. Also to allow folks the weekend to work. Lots of good submittals

The book is a comedy satire. It is poking fun at people and the value of a masters in business administration. It is also using current comedy to augment it.(such at toilet paper shortages) ..example: is also a chapter on Examples of who is a wizard of the fibbing crafts and why. There are also examples showing how you can become a wizard of the fibbing crafts.

• 1) Must have the logo on the back of the book in the corner.
2) must have the Author name on front: R.K. Holloway
3) These are the words for the back of the book:
This is a comedy. Well, more a satire if you are going to split hairs, but stop being a smarty-pants.
Step 1: Start drinking. This book is better that way.
Step 2: Go poop.
Step 3: ?????
Step 4: Profit!
"This is a must read!"
(or at least a great gag gift for your best bullshitting friends and family.)
"Laugh out loud funny!"
"No one is safe!"

```html
<!DOCTYPE html>
<html lang="en">
<head>
<meta charset="utf-8">
<title>Wizards of the Fibbing Crafts – Cover Wrap</title>
<link rel="stylesheet" href="https://fonts.googleapis.com/css2?family=Crimson+Pro:ital,wght@0,400;0,600;0,700;1,400&family=UnifrakturMaguntia&family=Tinos&display=swap">
<style>
  :root {
    --bg-light: #f1f1f2;
    --bg-dark: #d9d9db;
    --ink: #2a2a2a;
    --gold: #8c6422;
    --art-light: #f7f7f8;
    --art-mid: #e4e4e6;
    --rule: #7a7a7a;
    --navy: #2e3470;
    --seal: #c9a13d;
  }
  html, body { margin: 0; padding: 0; overflow: hidden; }
  .cover {
    position: relative;
    width: 1200px;
    height: 925px;
    overflow: hidden;
    background: radial-gradient(ellipse at 60% 45%, var(--bg-light) 0%, var(--bg-dark) 100%);
    font-family: "Crimson Pro", serif;
    color: var(--ink);
  }

  /* Back cover */
  .back-heading {
    position: absolute; left: 0; width: 540px; top: 138px;
    margin: 0; text-align: center;
    font-size: 54px; font-weight: 600; letter-spacing: -2px; line-height: 1;
  }
  .back-intro {
    position: absolute; left: 31px; top: 244px; width: 490px; margin: 0;
    font-size: 22px; line-height: 33px;
  }
  .steps {
    position: absolute; left: 44px; top: 340px; margin: 0; padding: 0;
    list-style: none; font-size: 22px; line-height: 32px;
  }
  .steps strong { font-weight: 700; }
  .praise {
    position: absolute; left: 31px; top: 501px; width: 490px; margin: 0;
    font-size: 22px; line-height: 32px;
  }
  .praise p { margin: 0; }
  .publisher {
    position: absolute; left: 33px; top: 842px;
    display: flex; align-items: center; gap: 8px;
    font-size: 18px; font-weight: 700; color: var(--navy);
  }
  .publisher .mark { width: 14px; height: 14px; background: var(--navy); }

  /* Spine */
  .spine-title, .spine-author {
    position: absolute; margin: 0; white-space: nowrap;
    writing-mode: vertical-rl; line-height: 1;
  }
  .spine-title { left: 583px; top: 58px; font-size: 35px; color: var(--gold); }
  .spine-author { left: 587px; top: 694px; font-size: 29px; }

  /* Front cover */
  .front-art { position: absolute; left: 0; top: 0; }
  .cert { position: absolute; margin: 0; text-align: center; }
  .cert-degree {
    left: 764px; width: 300px; top: 196px;
    font-family: "UnifrakturMaguntia", serif; font-size: 76px; color: var(--gold); line-height: 1;
  }
  .cert-title {
    left: 744px; width: 340px; top: 318px;
    font-size: 44px; font-weight: 700; line-height: 46px; color: var(--gold);
  }
  .cert-body {
    left: 774px; width: 280px; top: 477px;
    font-family: "Tinos", serif; font-size: 12.5px; line-height: 16px; color: #333;
  }
  .cert-sign {
    font-family: "Tinos", serif; font-size: 8px; color: #444; top: 644px;
  }
  .cert-sign.president { left: 780px; }
  .cert-sign.dean { left: 996px; }
  .part {
    position: absolute; left: 1032px; top: 740px;
    font-size: 30px; font-style: italic; color: #333;
  }
  .front-author {
    position: absolute; left: 740px; width: 370px; top: 850px; margin: 0;
    text-align: center; font-size: 48px; font-weight: 700; letter-spacing: -1px; line-height: 1;
  }
</style>
</head>
<body>
<div class="cover">
  <h2 class="back-heading">This is a comedy</h2>
  <p class="back-intro">Well, more a satire if you are going to split hairs, but stop being&nbsp; a smarty-pants.</p>
  <ul class="steps">
    <li><strong>Step 1</strong>: Start drinking. This book is better that way.</li>
    <li><strong>Step 2</strong>: Go poop.</li>
    <li><strong>Step 3</strong>: ?????</li>
    <li><strong>Step 4</strong>: Profit!</li>
  </ul>
  <div class="praise">
    <p>"This is a must read!"</p>
    <p>(or at least a great gag gift for your best bullshitting<br>friends and family.)</p>
    <p>"Laugh out loud funny!"</p>
    <p>"No one is safe!"</p>
  </div>
  <div class="publisher"><span class="mark"></span>Tallgate Press</div>

  <p class="spine-title">The Wizards of the Fibbing Crafts</p>
  <p class="spine-author">R.K. Holloway</p>

  <svg class="front-art" width="1200" height="925" viewBox="0 0 1200 925">
    <defs>
      <linearGradient id="artFill" x1="0" y1="0" x2="0" y2="1">
        <stop offset="0" stop-color="var(--art-light)"/>
        <stop offset="1" stop-color="var(--art-mid)"/>
      </linearGradient>
    </defs>
    <rect role="img" aria-label="Photo of a steel toilet-paper holder with an embossed sheet hanging down, printed like a diploma"
      x="700" y="28" width="470" height="802" rx="6" fill="url(#artFill)"/>
    <circle cx="916" cy="629" r="38" fill="var(--seal)"/>
    <line x1="742" y1="675" x2="1099" y2="675" stroke="var(--rule)" stroke-width="2"/>
    <line x1="742" y1="680" x2="1099" y2="680" stroke="#999" stroke-width="1"/>
  </svg>

  <div class="cert cert-degree">M.B.A.</div>
  <h1 class="cert cert-title">The Wizards<br>of the<br>Fibbing Crafts</h1>
  <p class="cert cert-body">with all the honor, rights, priveleges thereunto<br>appertaining in testimony whereof, we have<br>affixed our signatures with the<br>seal of the university</p>
  <span class="cert cert-sign president">President</span>
  <span class="cert cert-sign dean">Dean of Faculty</span>
  <span class="part">part 1</span>
  <p class="front-author">R.K. Holloway</p>
</div>
</body>
</html>
```